Custom Beer Labelling Company Needs a Flyer

We need a flyer designed to promote Hopwrapz, a new company in Sydney that helps home brewers create their own small batch beer labels. Main purpose of the flyer is to increase awareness of the service we offer and drive traffic to the Hopwrapz shopify site - www.hopwrapz-example.com.au.
Our value proposition is about being easy (less than 5 minutes), affordable (full set of labels from only $12) with good quality (water resistant synthetic labels that remove cleanly).
The flyer should suit A4 printing and will preferably include screenshot of the "Create your Label" tool on the site, and/or examples of our label templates. It may also include other information from our site such eg from the "About Us" or About Our Labels" pages.

Target Market(s)

Home brewers, mostly males aged 20-50

Industry/Entity Type

It Company

Colors
ec1f27
fee3d4
f9ba93
f68d4e
f37122
f78f20
faa54b
fbc994
ffffff

Requirements
Must have
• Drive customers to www.hopwrapz-example.com as call to action
Nice to have
• screenshot(s) and examples of labels

```html
<!DOCTYPE html>
<html lang="en">
<head>
<meta charset="utf-8">
<title>Hopwrapz Flyer</title>
<link href="https://fonts.googleapis.com/css2?family=Questrial&family=Roboto+Slab:wght@500;700&family=Ubuntu:wght@500;700&display=swap" rel="stylesheet">
<style>
  :root{
    --red:#ec1f27;
    --peach-pale:#fee3d4;
    --peach:#f9ba93;
    --orange-soft:#f68d4e;
    --orange-deep:#f37122;
    --orange:#f78f20;
    --orange-light:#faa54b;
    --sand:#fbc994;
    --white:#ffffff;
    --brown:#8a4a16;
    --amber-text:#c0661f;
    --ink:#2b2118;
    --band:#e5782a;
    --stage:#ebe6e3;
  }
  *{margin:0;padding:0;box-sizing:border-box}
  html,body{width:1041px;height:1200px;overflow:hidden}
  body{background:var(--stage);position:relative;font-family:'Questrial',sans-serif}
  .flyer{position:absolute;left:95px;top:0;width:850px;height:1200px;overflow:hidden;background:#fbeacb}
  .bottle-photo{position:absolute;left:0;top:0;width:850px;height:972px;
    background:
      radial-gradient(ellipse 60px 420px at 60px 620px, rgba(232,170,80,.45), transparent 70%),
      radial-gradient(ellipse 70px 460px at 250px 560px, rgba(232,170,80,.35), transparent 70%),
      radial-gradient(ellipse 70px 460px at 520px 540px, rgba(232,170,80,.35), transparent 70%),
      radial-gradient(ellipse 60px 440px at 790px 600px, rgba(232,170,80,.45), transparent 70%),
      linear-gradient(180deg,#fcf0d6 0%,#f8e0b0 55%,#f1c67e 100%)}
  .abs{position:absolute;left:0;width:100%;text-align:center;white-space:nowrap}
  .brand{top:40px;display:flex;justify-content:center;align-items:center;gap:16px}
  .brand-mark{width:62px;height:62px;background:var(--orange-deep)}
  .brand-name{font-family:'Roboto Slab',serif;font-weight:700;font-size:86px;line-height:1;color:var(--orange-deep)}
  .brand-rule{position:absolute;left:260px;top:150px;width:420px;height:3px;background:var(--orange)}
  .tagline-slab{top:158px;font-family:'Roboto Slab',serif;font-weight:700;font-size:27px;letter-spacing:1px;color:var(--brown);padding-left:90px}
  .lead{top:203px;font-size:31px;color:var(--ink)}
  .url-red{top:243px;font-family:'Ubuntu',sans-serif;font-weight:700;font-size:44px;color:var(--red)}
  .minutes{top:303px;font-family:'Ubuntu',sans-serif;font-weight:700;font-size:38px;color:var(--amber-text);letter-spacing:.5px}
  .price{top:345px;font-family:'Ubuntu',sans-serif;font-weight:700;font-size:60px;color:var(--red);letter-spacing:1px}
  .fullset{top:410px;font-size:35px;color:var(--orange-deep);letter-spacing:.5px}
  .fullset-rule{position:absolute;left:148px;top:455px;width:560px;height:2px;background:var(--orange)}
  .motto{top:467px;font-size:29px;color:var(--ink)}

  .laptop-screen{position:absolute;left:129px;top:536px;width:590px;height:398px;background:#111;border-radius:16px 16px 0 0;border:2px solid #555}
  .screen{position:absolute;left:31px;top:31px;width:526px;height:334px;background:#f4f2f0;overflow:hidden}
  .device-name{position:absolute;left:0;bottom:5px;width:100%;text-align:center;font-size:10px;color:#888}
  .laptop-base{position:absolute;left:38px;top:932px;width:773px;height:38px;border-radius:2px 2px 30px 30px;background:linear-gradient(180deg,#f2f2f2,#cfcfcf 60%,#9c9c9c)}
  .laptop-notch{position:absolute;left:50%;top:0;width:110px;height:7px;margin-left:-55px;background:#bbb;border-radius:0 0 8px 8px}

  .site-head{height:40px;display:flex;align-items:center;justify-content:space-between;padding:0 10px;background:var(--white)}
  .site-logo{display:flex;align-items:center;gap:5px;font-family:'Roboto Slab',serif;font-weight:700;font-size:20px;color:var(--orange-deep)}
  .site-logo i{display:block;width:14px;height:14px;background:var(--orange-deep)}
  .site-nav{font-size:7px;letter-spacing:1px;color:#9a7a5c}
  .site-body{position:absolute;top:40px;left:0;right:0;bottom:0;display:flex}
  .label-preview{width:247px;height:100%;background:linear-gradient(90deg,#5a1015,#9d1c24 30%,#7a1218 70%,#4a0c10)}
  .label-form{flex:1;padding:8px 10px;font-size:8px;color:#555}
  .form-title{font-size:15px;color:#444;font-weight:bold}
  .form-sub{font-size:8px;color:#888;margin-bottom:5px;font-family:'Roboto Slab',serif}
  .grid{display:grid;grid-template-columns:1fr 1fr;gap:3px 10px}
  .grid3{display:grid;grid-template-columns:1fr 1fr 1fr;gap:3px 8px;margin-top:3px}
  .field b{display:block;font-size:6px;letter-spacing:.5px;color:#555}
  .field span{display:block;height:15px;background:var(--white);border:1px solid #ddd;padding:2px 3px;font-size:8px}
  .notes{margin-top:3px}
  .notes span{height:26px;font-size:7px;line-height:1.3}
  .opts{display:flex;gap:10px;margin-top:4px;align-items:flex-end}
  .swatches{display:flex;gap:2px}
  .swatches i{width:14px;height:11px;display:block}
  .sizes{display:flex;gap:4px;background:var(--white);border:1px solid #ddd;padding:2px 6px;font-size:6px}
  .add-row{display:flex;align-items:center;gap:60px;margin-top:8px;padding-left:30px}
  .cost{font-size:13px;color:#555}
  .add-btn{background:var(--red);color:var(--white);font-size:9px;padding:4px 8px}

  .features{position:absolute;left:0;top:970px;width:850px;height:128px;background:var(--band)}
  .features svg{position:absolute;left:0;top:0}
  .feature{position:absolute;font-size:16.5px;line-height:1.3;color:var(--white)}
  .f1{left:40px;top:21px;width:230px;text-align:justify}
  .f2{left:305px;top:31px;width:212px}
  .f3{left:556px;top:21px;width:254px;text-align:justify}
  .cta{position:absolute;left:0;top:1101px;width:850px;height:99px;background:var(--orange);text-align:center;color:var(--white)}
  .cta-line{padding-top:16px;font-size:25px}
  .cta-url{font-size:35px;margin-top:2px;letter-spacing:.5px}
</style>
</head>
<body>
<main class="flyer">
  <div class="bottle-photo" role="img" aria-label="Photograph of chilled beer bottles with condensation"></div>

  <div class="abs brand"><span class="brand-mark"></span><span class="brand-name">Hopwrapz</span></div>
  <div class="brand-rule"></div>
  <div class="abs tagline-slab">BEST HOMEBREW LABELS</div>
  <div class="abs lead">Easy &amp; Affordable Small Batch Beer Labels At</div>
  <div class="abs url-red">www.hopwrapz-example.com.au</div>
  <div class="abs minutes">LESS THAN FIVE MINUTES AND</div>
  <div class="abs price">FROM JUST $12 FOR</div>
  <div class="abs fullset">A FULL SET OF CUSTOM PRINTED LABELS.</div>
  <div class="fullset-rule"></div>
  <div class="abs motto">Take Your Homebrew To Another Level.</div>

  <div class="laptop-screen">
    <div class="screen">
      <header class="site-head">
        <div class="site-logo"><i></i>Hopwrapz</div>
        <nav class="site-nav">CREATE YOUR LABEL &nbsp;|&nbsp; ABOUT US &nbsp;|&nbsp; ABOUT OUR LABELS &nbsp;|&nbsp; BLOG</nav>
      </header>
      <div class="site-body">
        <div class="label-preview" role="img" aria-label="Preview of a red beer label template with thumbnails of other designs"></div>
        <div class="label-form">
          <div class="form-title">CREATE YOUR LABEL</div>
          <div class="form-sub">easy and affordable small batch beer labels</div>
          <div class="grid">
            <div class="field"><b>BEER NAME</b><span>Your Beer</span></div>
            <div class="field"><b>STYLE</b><span>Beer Style</span></div>
            <div class="field"><b>BREWED BY</b><span>Your Brewery</span></div>
            <div class="field"><b>TAGLINE</b><span>Your Tagline</span></div>
          </div>
          <div class="grid3">
            <div class="field"><b>BREWED</b><span>08/05/16</span></div>
            <div class="field"><b>BOTTLED</b><span>18/05/16</span></div>
            <div class="field"><b>ABV</b><span>0.0%</span></div>
          </div>
          <div class="grid" style="margin-top:3px">
            <div class="field"><b>ORIGINAL GRAVITY</b><span>1010</span></div>
            <div class="field"><b>FINAL GRAVITY</b><span>1010</span></div>
          </div>
          <div class="field notes"><b>NOTES</b><span>This may include further brewing details such as grain bill, mash and sparge temperatures, boil time and hop additions</span></div>
          <div class="opts">
            <div class="field"><b>COLOR</b><div class="swatches"><i style="background:#111"></i><i style="background:#b9b38f"></i><i style="background:#7fb3b3"></i><i style="background:#b52a3a"></i></div></div>
            <div class="field"><b>ICON</b><div class="sizes">⚓ ★ ✲</div></div>
            <div class="field"><b>BOTTLE TYPE</b><div class="sizes"><span>Large</span><span>Small</span></div></div>
          </div>
          <div class="add-row"><span class="cost">$0.79</span><span class="add-btn">ADD</span></div>
        </div>
      </div>
    </div>
    <div class="device-name">MoonBook</div>
  </div>
  <div class="laptop-base"><div class="laptop-notch"></div></div>

  <section class="features">
    <svg width="850" height="128" viewBox="0 0 850 128">
      <polyline points="278,0 288,64 278,128" fill="none" stroke="#f9ba93" stroke-width="2"/>
      <polyline points="528,0 538,64 528,128" fill="none" stroke="#f9ba93" stroke-width="2"/>
    </svg>
    <p class="feature f1">Just fill in template with details of your brew, and select from our range of designs, colours, icons and bottle size.</p>
    <p class="feature f2">We print your labels in high quality LED on A4 sheets of die cut, self-adhesive labels</p>
    <p class="feature f3">Our synthetic labels are water resistant and remove cleanly from your empties without tearing and without leftover glue crud.</p>
  </section>
  <footer class="cta">
    <div class="cta-line">Try A Set Of Hopwrapz Next Time You Lay Down A Batch.</div>
    <div class="cta-url">www.hopwrapz-example.com.au</div>
  </footer>
</main>
</body>
</html>
```